Business Cards for Law Office of Denise R. Harlow

I need a business card for my new estate planning law firm. I have attached my logo. I would like a design that is professional but not too formal or stuffy.

Target Market(s)

Professionals (lawyers, doctors, businesswomen) between the age of 30 and 50 who are tech-savvy and educated.

Industry/Entity Type

Lawyer

Contact Information for Business Card

Denise R. Harlow

528 E. 19th Street
7th Floor
New York, NY 10583

Phone: (855) 602-7318
Direct: (917) 463-5071
Email: Denise@DeniseRHarlowLegal.test
www.DeniseRHarlowLegal.test

Font styles to use
Other font styles liked:
• Corbel

Requirements
Must have
• On the front:
• Denise R. Harlow, Esq.
• Owner & Founder
• 528 E. 19th Street
• 7th Floor
• New York, NY 10583
• Phone: (855) 602-7318
• Direct: (917) 463-5071
• Email: denise@deniserharlowlegal.test
• www.deniserharlowlegal.test
• On the back:
• LOGO
Nice to have
• I want it to be professional but not too formal or stuffy. Please choose colors that go with my logo.
Should not have
• I don't want TOO MUCH color. Some color is good, but not too much.

```html
<!DOCTYPE html>
<html lang="en">
<head>
<meta charset="utf-8">
<title>Business Cards – Law Office of Denise R. Harlow</title>
<link href="https://fonts.googleapis.com/css2?family=Open+Sans:wght@400;600&family=Tinos:wght@700&display=swap" rel="stylesheet">
<style>
  :root {
    --backdrop: #7c7c7c;
    --card-white: #ffffff;
    --plum: #7b2a7e;
    --ink: #2a2a2a;
    --slate-dark: #27353e;
    --slate: #35464f;
    --slate-light: #4d606a;
    --peach: #f2b48a;
  }
  * { margin: 0; padding: 0; box-sizing: border-box; }
  html, body { width: 1200px; height: 900px; overflow: hidden; }
  body {
    background: var(--backdrop);
    position: relative;
    font-family: "Open Sans", sans-serif;
  }
  .card {
    position: absolute;
    top: 170px;
    width: 347px;
    height: 561px;
  }
  .card-front { left: 259px; background: var(--card-white); }
  .card-back {
    left: 631px;
    background: linear-gradient(180deg, var(--slate-dark) 0%, var(--slate) 100%);
  }
  .tab {
    position: absolute;
    left: 104px;
    width: 139px;
    height: 31px;
    background: var(--plum);
  }
  .tab-top { top: 0; }
  .tab-bottom { bottom: 0; }
  .firm-name {
    position: absolute;
    left: 0; right: 0;
    text-align: center;
    font-family: "Open Sans", sans-serif;
    font-weight: 600;
    color: var(--plum);
    letter-spacing: 0.5px;
  }
  .card-front .firm-name {
    top: 122px;
    font-size: 21px;
    line-height: 28px;
  }
  .holder {
    position: absolute;
    top: 270px;
    left: 0; right: 0;
    text-align: center;
  }
  .holder-name {
    font-family: "Tinos", serif;
    font-weight: 700;
    font-size: 19px;
    color: var(--plum);
    letter-spacing: 0.6px;
    text-transform: uppercase;
  }
  .holder-title {
    font-size: 14.5px;
    color: var(--ink);
    margin-top: 1px;
  }
  .contact-icons {
    position: absolute;
    top: 342px;
    left: 0; right: 0;
    display: flex;
    justify-content: center;
    gap: 8px;
  }
  .contact-icons svg { width: 11px; height: 10px; fill: var(--plum); }
  .contact-lines, .address {
    position: absolute;
    left: 0; right: 0;
    text-align: center;
    font-size: 14.5px;
    line-height: 20.5px;
    color: var(--ink);
  }
  .contact-lines { top: 361px; }
  .address { top: 446px; }
  .photo-band {
    position: absolute;
    top: 143px;
    left: 0;
    width: 347px;
    height: 275px;
    background: linear-gradient(90deg, var(--slate-light) 0%, #5d717b 45%, #6f838c 100%);
  }
  .card-back .firm-name {
    top: 259px;
    font-size: 22px;
    line-height: 30px;
  }
</style>
</head>
<body>
  <section class="card card-front">
    <div class="tab tab-top"></div>
    <div class="firm-name">Law Office of<br>Denise R. Harlow</div>
    <div class="holder">
      <div class="holder-name">Denise R. Harlow, Esq.</div>
      <div class="holder-title">Owner &amp; Founder</div>
    </div>
    <div class="contact-icons">
      <svg viewBox="0 0 12 10" aria-hidden="true"><path d="M1 3c0-1.5 2-2.5 5-2.5S11 1.5 11 3v1H8.5V3h-5v1H1z M2.5 5h7l1 4h-9z M6 5.8a1.3 1.3 0 1 0 0 2.6a1.3 1.3 0 1 0 0-2.6z"/></svg>
      <svg viewBox="0 0 12 10" aria-hidden="true"><path d="M1 3c0-1.5 2-2.5 5-2.5S11 1.5 11 3v1H8.5V3h-5v1H1z M2.5 5h7l1 4h-9z M6 5.8a1.3 1.3 0 1 0 0 2.6a1.3 1.3 0 1 0 0-2.6z"/></svg>
      <svg viewBox="0 0 12 10" aria-hidden="true"><path d="M0.5 1h11v8h-11z M1.5 2v0.4L6 5.6l4.5-3.2V2z" fill-rule="evenodd"/></svg>
    </div>
    <div class="contact-lines">
      (855) 602-7318<br>
      (917) 463-5071(Direct)<br>
      denise@deniserharlowlegal.test
    </div>
    <div class="address">
      528 E. 19th Street<br>
      7th Floor New York, NY 10583
    </div>
    <div class="tab tab-bottom"></div>
  </section>

  <section class="card card-back">
    <div class="photo-band" role="img" aria-label="Photo of a modern glass-walled office interior"></div>
    <div class="firm-name">Law Office of<br>Denise R. Harlow</div>
  </section>
</body>
</html>
```